Dental Practice Billboard Design

We are a newer dental practice in need of a simple but appealing billboard for our growing dental practice to attract new patients. The practice is owned by husband and wife dentists and is family friendly in a small town in Kentucky. We try to be very friendly and caring to our patients. Would prefer a blue background for the billboard and our tooth logo to be prominent. We are partial to the Patua One font used in the image below but please feel free to tweak it as you deem necessary. The shape of the uppercase D and lowercase g are why we like that font, so fonts with a similarly shaped “D” and “g” would work as well. Please include our phone number (606) 847-3190. Please see our website Halvorcrestdentistry.com for more info on the practice if needed. Thank you! Looking forward to seeing your creation.
Updates

The dimensions will be 12ft x 24ft (3.6576m x 7.3152m). Apologies for not including this in the original prompt. Thank you all for your submissions.

Industry/Entity Type

Dental

Font styles to use
Other font styles liked:
• Patua One

Colors
0054AA
0677BA
7BADD7
CADEEF
E8F1F8
0094D4
00A9DD
6FCCEA
C7EBF8
E9F6FB
00AB8E
00BBA5
67D7C9
C6EFE9
E9F9F6
59FF00
82FF00
B8FF75
E3FFCB
F4FFEA

Requirements
Must have
• Phone number, website, Logo, Practice name “Halvor Crest Dentistry”
Should not have
• A tagline or slogan

```html
<!DOCTYPE html>
<html lang="en">
<head>
<meta charset="UTF-8">
<title>Halvor Crest Dentistry Billboard</title>
<link rel="stylesheet" href="https://fonts.googleapis.com/css2?family=Montserrat:wght@700&family=Patua+One&family=Roboto+Condensed:wght@700&display=swap">
<style>
  :root {
    --page: #e9eef5;
    --navy: #243a86;
    --white: #ffffff;
    --green: #62b83e;
    --teal: #4fb8ad;
  }
  * { margin: 0; padding: 0; box-sizing: border-box; }
  html, body {
    width: 1200px;
    height: 1000px;
    overflow: hidden;
    background: var(--page);
  }
  .billboard {
    position: absolute;
    left: 0;
    top: 199px;
    width: 1200px;
    height: 602px;
    background: var(--navy);
    color: var(--white);
    overflow: hidden;
  }
  .services {
    position: absolute;
    top: 62px;
    font-family: "Montserrat", sans-serif;
    font-weight: 700;
    list-style: none;
  }
  .services--left { left: 85px; }
  .services--right { left: 891px; }
  .services__title {
    color: var(--green);
    font-size: 22px;
    line-height: 32px;
  }
  .services__item {
    display: flex;
    align-items: center;
    gap: 5px;
    font-size: 22px;
    line-height: 32px;
    white-space: nowrap;
  }
  .services__icon { width: 14px; height: 14px; flex: none; }
  .brand-mark {
    position: absolute;
    left: 0;
    width: 1200px;
    top: 150px;
    display: flex;
    justify-content: center;
    align-items: center;
    gap: 12px;
    font-family: "Patua One", serif;
    font-size: 30px;
    color: var(--white);
    white-space: nowrap;
  }
  .brand-mark__dot {
    width: 22px;
    height: 22px;
    border-radius: 50%;
    background: var(--green);
  }
  .practice-name {
    position: absolute;
    left: 0;
    width: 1200px;
    top: 305px;
    text-align: center;
    font-family: "Patua One", serif;
    font-size: 84px;
    line-height: 100px;
    font-weight: 400;
    white-space: nowrap;
  }
  .divider {
    position: absolute;
    left: 95px;
    width: 1010px;
    top: 411px;
    height: 2px;
    background: linear-gradient(90deg, transparent, var(--white) 20%, var(--white) 80%, transparent);
  }
  .website {
    position: absolute;
    left: 0;
    width: 1200px;
    top: 422px;
    text-align: center;
    font-family: "Patua One", serif;
    font-size: 33px;
    line-height: 42px;
    color: var(--green);
    white-space: nowrap;
  }
  .band-rule {
    position: absolute;
    left: 0;
    width: 1200px;
    top: 478px;
    height: 4px;
    background: var(--green);
  }
  .call {
    position: absolute;
    left: 0;
    width: 1200px;
    top: 482px;
    height: 120px;
    display: flex;
    justify-content: center;
    align-items: center;
    gap: 30px;
    font-family: "Roboto Condensed", sans-serif;
    font-weight: 700;
    font-size: 88px;
    line-height: 1;
    white-space: nowrap;
  }
  .call__prompt { color: var(--teal); }
  .call__phone { color: var(--white); }
</style>
</head>
<body>
  <main class="billboard">
    <ul class="services services--left">
      <li class="services__title">Our Services</li>
      <li class="services__item"><svg class="services__icon" viewBox="0 0 14 14"><path d="M2 7.5 L5.5 11 L12 3" fill="none" stroke="#ffffff" stroke-width="2"/></svg>Crowns</li>
      <li class="services__item"><svg class="services__icon" viewBox="0 0 14 14"><path d="M2 7.5 L5.5 11 L12 3" fill="none" stroke="#ffffff" stroke-width="2"/></svg>Root Canals</li>
      <li class="services__item"><svg class="services__icon" viewBox="0 0 14 14"><path d="M2 7.5 L5.5 11 L12 3" fill="none" stroke="#ffffff" stroke-width="2"/></svg>Extractions</li>
      <li class="services__item"><svg class="services__icon" viewBox="0 0 14 14"><path d="M2 7.5 L5.5 11 L12 3" fill="none" stroke="#ffffff" stroke-width="2"/></svg>Implants</li>
      <li class="services__item"><svg class="services__icon" viewBox="0 0 14 14"><path d="M2 7.5 L5.5 11 L12 3" fill="none" stroke="#ffffff" stroke-width="2"/></svg>Bridges</li>
      <li class="services__item"><svg class="services__icon" viewBox="0 0 14 14"><path d="M2 7.5 L5.5 11 L12 3" fill="none" stroke="#ffffff" stroke-width="2"/></svg>Clear Aligner</li>
    </ul>

    <div class="brand-mark">
      <span class="brand-mark__dot"></span>
      <span class="brand-mark__name">Halvor Crest Dentistry</span>
    </div>

    <ul class="services services--right">
      <li class="services__title">Our Services</li>
      <li class="services__item"><svg class="services__icon" viewBox="0 0 14 14"><path d="M2 7.5 L5.5 11 L12 3" fill="none" stroke="#ffffff" stroke-width="2"/></svg>Veneers</li>
      <li class="services__item"><svg class="services__icon" viewBox="0 0 14 14"><path d="M2 7.5 L5.5 11 L12 3" fill="none" stroke="#ffffff" stroke-width="2"/></svg>Whitening</li>
      <li class="services__item"><svg class="services__icon" viewBox="0 0 14 14"><path d="M2 7.5 L5.5 11 L12 3" fill="none" stroke="#ffffff" stroke-width="2"/></svg>Fillings</li>
      <li class="services__item"><svg class="services__icon" viewBox="0 0 14 14"><path d="M2 7.5 L5.5 11 L12 3" fill="none" stroke="#ffffff" stroke-width="2"/></svg>Cleanings</li>
      <li class="services__item"><svg class="services__icon" viewBox="0 0 14 14"><path d="M2 7.5 L5.5 11 L12 3" fill="none" stroke="#ffffff" stroke-width="2"/></svg>Dentures</li>
      <li class="services__item"><svg class="services__icon" viewBox="0 0 14 14"><path d="M2 7.5 L5.5 11 L12 3" fill="none" stroke="#ffffff" stroke-width="2"/></svg>Overdentures</li>
    </ul>

    <h1 class="practice-name">Halvor Crest Dentistry</h1>
    <div class="divider"></div>
    <p class="website">Halvorcrestdentistry.com</p>
    <div class="band-rule"></div>
    <p class="call">
      <span class="call__prompt">CALL TODAY!</span>
      <span class="call__phone">(606) 847-3190</span>
    </p>
  </main>
</body>
</html>
```